Website design with eCommerce for revolutionary new product in the manufacturing industry.

We need a website designed for a precision manufacturing company based in the suburbs of Minneapolis, Minnesota called Velk Manufacturing. We have a revolutionary new product, the TREMLA, to introduce and sell through an eCommerce storefront. The website would include company information, product information, and the storefront. Green is a color that represents Velk Manufacturing. The final design should communicate that we exclusively offer premium products at a premium price. The design should also let the customer know they are the focus of our work.

Target Market(s)

Machinists and machine shops

Industry/Entity Type

Manufacturing and machine shops

Coding

Coded - Design and coding required

Font styles to use
Sans Serif

Colors
59FF00
82FF00
B8FF75
E3FFCB
F4FFEA

Requirements
Must have
• eCommerce storefront, Made in USA references
Nice to have
• Home page, TREMLA Product page, About Us, Capabilities, Contact, etc.
Should not have
• Should not be too much text and reading.

```html
<!DOCTYPE html>
<html lang="en">
<head>
<meta charset="utf-8">
<title>TREMLA · Velk Manufacturing</title>
<link rel="stylesheet" href="https://fonts.googleapis.com/css2?family=Saira:wght@500;600;700&family=Outfit:wght@400;500&display=swap">
<style>
:root{
  --green:#2e9f2b;
  --green-bright:#3cb534;
  --green-deep:#1d6b1a;
  --ink:#ffffff;
  --bg-black:#0b0b0b;
  --bg-dark:#231f20;
  --bg-deep:#141414;
  --field:#3a3a3a;
}
*{margin:0;padding:0;box-sizing:border-box}
html,body{width:670px;height:1200px;overflow:hidden;background:var(--bg-black)}
body{position:relative;font-family:"Outfit",sans-serif;color:var(--ink)}
.abs{position:absolute}
.display{font-family:"Saira",sans-serif;font-weight:600;text-transform:uppercase;letter-spacing:.02em}
.band{position:absolute;left:0;width:670px}
.header{top:0;height:35px;background:var(--bg-black)}
.hero{top:35px;height:262px;background:radial-gradient(ellipse at 40% 55%,#5a5756 0%,#3a3838 45%,#1c1b1b 100%)}
.why{top:297px;height:261px;background:var(--bg-dark)}
.what{top:558px;height:227px;background:var(--bg-deep)}
.better{top:785px;height:233px;background:var(--bg-dark)}
.footer{top:1018px;height:182px;background:var(--bg-black)}
.brand{font-family:"Saira",sans-serif;font-weight:700;color:#fff;letter-spacing:.06em}
.nav a{position:absolute;top:13px;font-family:"Saira",sans-serif;font-weight:600;font-size:6.2px;color:#fff;text-decoration:none;letter-spacing:.04em}
.nav a.current{color:var(--green-bright)}
.btn{position:absolute;display:flex;align-items:center;justify-content:center;font-family:"Saira",sans-serif;font-weight:600;font-size:6px;letter-spacing:.04em;text-transform:uppercase;border-radius:1px;color:#fff;background:var(--green);text-decoration:none}
.btn.outline{background:transparent;border:1px solid var(--green);color:var(--green-bright)}
.media{position:absolute;border-radius:4px}
.product{background:linear-gradient(155deg,#46c43c 0%,var(--green) 45%,var(--green-deep) 100%);box-shadow:0 6px 14px rgba(0,0,0,.45)}
.foam{background:linear-gradient(135deg,#3c3c3c,#1f1f1f);border-radius:1px}
.parts{background:linear-gradient(145deg,#d2d2d2,#8a8a8a 45%,#bdbdbd 70%,#6d6d6d);border:2px solid #6a4a2a;border-radius:1px}
h2.display{position:absolute;font-size:13px;line-height:1}
.copy{position:absolute;font-size:6.1px;line-height:8.4px;color:#fff}
.list{position:absolute;list-style:none;font-size:6.6px;line-height:8.4px}
.list li{position:relative;padding-left:12px;margin-bottom:2px}
.list li::before{content:"→";position:absolute;left:0;color:var(--green-bright);font-size:6px}
.ftitle{position:absolute;font-family:"Saira",sans-serif;font-weight:600;font-size:6.6px;letter-spacing:.04em}
.field{position:absolute;background:var(--field);font-size:5.4px;color:#e6e6e6;padding:3px 6px}
.social{position:absolute;top:1143px;width:17px;height:17px;border-radius:50%;background:#fff}
.social.active{background:var(--green)}
.bottom a{position:absolute;top:1183px;font-size:6.2px;color:#fff;text-decoration:none}
</style>
</head>
<body>

<header class="band header">
  <div class="abs brand" style="left:52px;top:8px;font-size:15px;line-height:20px">TREMLA</div>
  <nav class="nav">
    <a class="current" style="left:253px">-- HOME --</a>
    <a style="left:307px">CAPABILITIES</a>
    <a style="left:368px">ABOUT US</a>
    <a style="left:419px">GALLERY</a>
    <a style="left:466px">WISDOM</a>
  </nav>
  <a class="btn" style="left:506px;top:9px;width:56px;height:17px">Contact Us</a>
  <a class="btn outline" style="left:569px;top:9px;width:48px;height:17px;gap:4px">
    <svg width="7" height="6" viewBox="0 0 7 6"><path d="M0 .5h1.2l1 3.3h3.6L6.6 1.4H1.7" fill="none" stroke="currentColor" stroke-width=".7"/><circle cx="2.6" cy="5.2" r=".5" fill="currentColor"/><circle cx="5.3" cy="5.2" r=".5" fill="currentColor"/></svg>$0.00</a>
</header>

<section class="band hero">
  <p class="abs display" style="left:112px;top:64px;font-size:8.6px">Welcome to Velk Manufacturing</p>
  <h1 class="abs display" style="left:112px;top:83px;font-size:17px;line-height:20.2px;width:262px">We are a machine shop with complete end to end manufacturing capabilities.</h1>
  <a class="btn" style="left:112px;top:178px;width:56px;height:17px">About Us</a>
  <div class="media product" role="img" aria-label="Green TREMLA machined tool with steel rod" style="left:418px;top:36px;width:140px;height:188px"></div>
</section>

<section class="band why">
  <div class="media foam" role="img" aria-label="TREMLA tool in a foam case" style="left:112px;top:44px;width:84px;height:66px"></div>
  <div class="media foam" role="img" aria-label="TREMLA tool and hex key in a foam case" style="left:112px;top:124px;width:84px;height:66px"></div>
  <div class="media product" role="img" aria-label="Green TREMLA tool rendering" style="left:204px;top:36px;width:114px;height:162px"></div>
  <h2 class="display" style="left:342px;top:62px">Why Velk Manufacturing?</h2>
  <p class="copy" style="left:342px;top:83px;width:220px;line-height:7.6px;font-size:5.9px">Because there is a better way, and we will find it, even if it's the hard way. We believe in working harder and smarter to achieve success.</p>
  <ul class="list" style="left:342px;top:107px">
    <li>Our success is measured in your success</li>
    <li>Focused on our your needs and making excellent parts</li>
    <li>Exceeding your expectations</li>
  </ul>
  <a class="btn outline" style="left:342px;top:152px;width:56px;height:18px">Contact Us</a>
</section>

<section class="band what">
  <h2 class="display" style="left:112px;top:37px">What We Do</h2>
  <p class="copy" style="left:112px;top:59px;width:256px">We are a machine shop with complete end to end manufacturing capabilities. We can take an idea or need, and bring it to a complete physical product. We can design and build your prototype, and we can mass produce it too.</p>
  <p class="copy" style="left:112px;top:92px;width:256px">We love working directly with customers to manufacture their products, and help make it better where appropriate. We can work with as little as a verbal description, up to following fully defined customer specifications.</p>
  <p class="copy" style="left:112px;top:126px;width:256px">We work in a wide variety of materials, and are very good at creating fixture designs to address your process issues. We can even come to your business and help you make improvements onsite. We have helped many other machine shops be more successful.</p>
  <a class="btn" style="left:112px;top:171px;width:56px;height:17px">Contact Us</a>
</section>

<section class="band better">
  <h2 class="display" style="left:112px;top:33px;width:216px;text-align:center">How We Make It Better</h2>
  <div class="media product" role="img" aria-label="Green TREMLA tool shown at an angle" style="left:164px;top:68px;width:108px;height:126px"></div>
  <ul class="list" style="left:342px;top:37px;width:215px;font-size:6.2px;line-height:8.4px">
    <li>With 100 years of combined knowledge and experience to draw upon, we find solutions.</li>
    <li>Our vast experience across multiple industries gives us insight that is invaluable in creativity and foresight.</li>
    <li>This real life experience brings a broader understanding of what works, and more importantly, what doesn't work, ultimately allowing us to make more informed decisions.</li>
    <li>We consider the smallest details, and envision all the consequences in order to create a better product the first time.</li>
    <li>By recognizing risks early, we can address them before they become issues.</li>
    <li>We continuously improve and learn new things by staying up to date with emerging technologies and techniques.</li>
  </ul>
  <a class="btn outline" style="left:342px;top:180px;width:56px;height:18px">Contact Us</a>
</section>

<div class="media parts" role="img" aria-label="Tray of polished machined aluminium parts" style="left:398px;top:531px;width:160px;height:219px;z-index:3"></div>

<svg class="abs" width="670" height="1200" style="left:0;top:0;z-index:2;pointer-events:none" aria-hidden="true">
  <g fill="#2e9f2b">
    <polygon points="228,35 238,25.5 238,32 670,32 670,38 238,38 238,44.5"/>
    <polygon points="0,294 432,294 432,287.5 442,297 432,306.5 432,300 0,300"/>
    <polygon points="228,558 238,548.5 238,555 670,555 670,561 238,561 238,567.5"/>
    <polygon points="0,782 432,782 432,775.5 442,785 432,794.5 432,788 0,788"/>
    <polygon points="228,1018 238,1008.5 238,1015 670,1015 670,1021 238,1021 238,1027.5"/>
  </g>
</svg>

<footer class="band footer">
  <div class="abs brand" style="left:112px;top:27px;font-size:17px;line-height:22px">TREMLA</div>
  <div class="abs" style="left:132px;top:70px;display:flex;align-items:center;gap:5px">
    <span style="width:9px;height:9px;background:#fff;display:block"></span>
    <span class="brand" style="font-size:9px">VELK MFG</span>
  </div>

  <p class="ftitle" style="left:265px;top:28px">CONTACT US</p>
  <p class="abs" style="left:265px;top:42px;font-size:8.6px;color:var(--green-bright)">Call: 123-456-7890</p>
  <p class="abs" style="left:265px;top:55px;font-size:6.4px">info@tremlamfg.com</p>
  <p class="abs" style="left:265px;top:71px;font-size:5.8px;color:var(--green-bright);font-family:'Saira',sans-serif;font-weight:600">ADDRESS:</p>
  <p class="abs" style="left:265px;top:79px;font-size:6.6px;line-height:8.5px">Lorem ipsum work 195 N-4646<br>work design - 1234</p>
  <p class="ftitle" style="left:265px;top:114px;color:var(--green-bright)">FOLLOW US</p>
</footer>
<a class="social" aria-label="Social profile one" style="left:265px"></a>
<a class="social active" aria-label="Social profile two" style="left:286px"></a>
<a class="social" aria-label="Social profile three" style="left:307px"></a>

<p class="ftitle" style="left:401px;top:1046px">SEND US MESSAGE</p>
<div class="field" style="left:401px;top:1062px;width:76px;height:15px">Name</div>
<div class="field" style="left:484px;top:1062px;width:75px;height:15px">Phone</div>
<div class="field" style="left:401px;top:1084px;width:158px;height:14px">Email</div>
<div class="field" style="left:401px;top:1105px;width:158px;height:31px">Message</div>
<a class="btn" style="left:401px;top:1143px;width:50px;height:17px">Send</a>

<div class="abs" style="left:112px;top:1175px;width:447px;height:1px;background:#333"></div>
<p class="abs" style="left:112px;top:1183px;font-size:6.2px">© 2022 <span style="color:var(--green-bright)">TREMLA.</span> All Right Reserved · Made in USA</p>
<nav class="bottom">
  <a style="left:265px;color:var(--green-bright)">– Home –</a>
  <a style="left:313px">Capabilities</a>
  <a style="left:361px">About Us</a>
  <a style="left:403px">Gallery</a>
  <a style="left:438px">Wisdom</a>
  <a style="left:477px">Contact Us</a>
</nav>
<svg class="abs" style="left:572px;top:1170px" width="11" height="13" viewBox="0 0 11 13" aria-label="Back to top"><path d="M5.5 1L1 12l4.5-3 4.5 3z" fill="none" stroke="#3cb534" stroke-width="1"/></svg>

</body>
</html>
```